My new Bible based podcast needs a Podcast Cover Design for Vexora directory

I need a Podcast Cover Design design for my podcast listing in Vexora. The podcast is called Morning Lanterns Over Hills. I would like something cheerful, warm, and fresh because I take a non-traditional approach to explaining how the Bible is relevant to people today. My goal is to get back to the original spirituality of the Bible without all the centuries of added man-made doctrines. It would be great to show a sense of peace and hope, with new possibilities. This is not like a floating corporate logo. I need it to be square and full color/design all the way to the edges.

I have resubmitted this project because I did not understand how to ask for a podcast cover design. If you already submitted for me, I apologize for not knowing how the system works. I did not give the best picture of what I needed.

Target Market(s)

People who want a fresh look at the Bible

Industry/Entity Type

Religious

Logo Text

Morning Lanterns Over Hills

Colors

Designer to choose colors to be used in the design.

Requirements
Must have
• It must be square. The design should fill the space. See screen shot below of podcast cover designs on the Christianity/Spirituality page of Vexora directory so you can see where the podcast cover design needs to fit in and stand out.
• The final design will need to be:
• 3,000 x 3,000 pixels (but readable at 150 x 150)
• 72 dpi
• .jpg or .png format
• rgb color space
Nice to have
• Perhaps an open book suggesting the Bible, but not necessary.
Should not have
• No microphones or airwaves.

```html
<!DOCTYPE html>
<html lang="en">
<head>
<meta charset="utf-8">
<title>Morning Lanterns Over Hills — Podcast Cover</title>
<link rel="stylesheet" href="https://fonts.googleapis.com/css2?family=Jost:wght@400;700;900&display=swap">
<style>
  :root {
    --sun-yellow: #ffd21c;
    --sun-yellow-light: #ffe02a;
    --sun-yellow-deep: #fcc214;
    --ember-orange: #ff8c1a;
    --ember-orange-soft: #ffa51f;
    --ink-white: #ffffff;
  }
  html, body {
    margin: 0;
    padding: 0;
    width: 1200px;
    height: 1200px;
    overflow: hidden;
  }
  .cover {
    position: relative;
    width: 1200px;
    height: 1200px;
    overflow: hidden;
    background: linear-gradient(180deg, var(--sun-yellow-light) 0%, var(--sun-yellow) 45%, var(--sun-yellow-deep) 100%);
    font-family: "Jost", "Futura", sans-serif;
    color: var(--ink-white);
  }
  .cover__scene {
    position: absolute;
    inset: 0;
    width: 1200px;
    height: 1200px;
  }
  .title {
    position: absolute;
    left: 0;
    top: 0;
    width: 760px;
    height: 1200px;
    margin: 0;
    font-weight: 400;
  }
  .title__line {
    position: absolute;
    display: block;
    line-height: 1;
    white-space: nowrap;
  }
  .title__line--light {
    font-weight: 400;
    font-size: 128px;
    letter-spacing: -2px;
  }
  .title__line--first { left: 90px; top: 240px; }
  .title__line--third { left: 100px; top: 545px; }
  .title__line--hero {
    left: 102px;
    top: 392px;
    font-weight: 900;
    font-size: 117px;
    letter-spacing: -1px;
  }
  .title__line--last {
    right: 68px;
    top: 660px;
    font-weight: 700;
    font-size: 148px;
    letter-spacing: -2px;
  }
  .divider {
    position: absolute;
    left: 765px;
    top: 272px;
    width: 6px;
    height: 525px;
    background: var(--ink-white);
  }
</style>
</head>
<body>
  <main class="cover">
    <svg class="cover__scene" viewBox="0 0 1200 1200" role="img" aria-label="Warm yellow duotone photo of a person in a straw hat sitting on a sandy beach, gazing out over the sea">
      <defs>
        <linearGradient id="figureTone" x1="0" y1="0" x2="0" y2="1">
          <stop offset="0" stop-color="#ffe52a"/>
          <stop offset="0.3" stop-color="#ff9a1c"/>
          <stop offset="1" stop-color="#ff8c1a"/>
        </linearGradient>
        <radialGradient id="figureGlow" cx="0.6" cy="0.55" r="0.6">
          <stop offset="0" stop-color="#ff8c1a" stop-opacity="0.9"/>
          <stop offset="1" stop-color="#ffa51f" stop-opacity="0"/>
        </radialGradient>
      </defs>
      <rect x="0" y="260" width="1200" height="700" fill="#ffcf1a" opacity="0.35"/>
      <rect x="760" y="260" width="440" height="860" rx="180" fill="url(#figureGlow)"/>
      <rect x="860" y="440" width="340" height="620" rx="150" fill="url(#figureTone)" opacity="0.85"/>
    </svg>

    <h1 class="title" aria-label="Morning Lanterns Over Hills">
      <span class="title__line title__line--light title__line--first">Morning</span>
      <span class="title__line title__line--hero">LANTERNS</span>
      <span class="title__line title__line--light title__line--third">Over</span>
      <span class="title__line title__line--last">Hills</span>
    </h1>

    <div class="divider"></div>
  </main>
</body>
</html>
```